Website Design for Architecture Practice

I need a home page and one sidebar/content page for an Architecture practice delivered in PSD.

This archictecture practice specialises in one-off, high end homes and commercial properties (restaurant) heavily influenced by Dorian Vessey Kent, particularly his work on the Tarrowby Museum

I am looking for a home page, and a generic content page where we can outline our services, and showcase our homes.

http://notes.qorvenuni.edu.au/studio/Tarrowby%20Lisdane%202.jpg

Target Market(s)

30-70yr old (typically wealthy) property buyers, developers and investors

Industry/Entity Type

Architecture

Number of Pages Required

2 page

Font styles to use
Serif
Sans Serif

Requirements
Must have
• Home page design
• a Content Page design (ie, top nav with sidebar)
Nice to have
• Use any Dorian Vessey Kent images you can find via google etc as placeholders for our own photography (ie they don't need to be licensed as we will be replacing with our own commissioned photography). Full color preferred but feel free to experiment with treating any images as you see fit.

```html
<!DOCTYPE html>
<html lang="en">
<head>
<meta charset="utf-8">
<title>Corvane Architects</title>
<link href="https://fonts.googleapis.com/css2?family=Marcellus&family=Open+Sans:wght@400;600&display=swap" rel="stylesheet">
<style>
:root{
  --red:#c3202c;
  --ink:#333333;
  --grey:#777777;
  --footer:#2a2a2a;
  --footer-bottom:#1c1c1c;
  --white:#ffffff;
}
*{box-sizing:border-box;margin:0;padding:0}
html,body{width:736px;height:1200px;overflow:hidden;background:var(--white)}
body{font-family:"Open Sans",Arial,sans-serif;color:var(--ink);position:relative}
.serif{font-family:"Marcellus",Georgia,serif}

/* header */
.site-header{position:absolute;left:0;top:0;width:736px;height:80px;background:var(--white)}
.brand{position:absolute;left:150px;top:14px;display:flex;flex-direction:column;align-items:center;gap:4px}
.brand-mark{width:26px;height:26px;background:var(--red)}
.brand-name{font-family:"Marcellus",Georgia,serif;color:var(--red);font-size:17px;line-height:20px;white-space:nowrap}
.phone{position:absolute;right:40px;top:14px;font-size:10px;color:var(--ink);display:flex;align-items:center;gap:5px}
.main-nav{position:absolute;right:40px;top:40px;display:flex;gap:2px}
.main-nav a{font-size:10px;color:var(--ink);text-decoration:none;padding:5px 9px;font-family:"Marcellus",Georgia,serif}
.main-nav a.active{background:var(--ink);color:var(--white)}

/* hero */
.hero{position:absolute;left:0;top:80px;width:736px;height:316px;background:linear-gradient(120deg,#3d2a1e 0%,#7a5236 35%,#a97a4f 55%,#5a3a26 80%,#2e2018 100%)}
.hero-caption{position:absolute;left:0;right:0;top:246px;text-align:center;color:var(--white);font-size:16px;line-height:20px}
.hero-caption .rule{display:inline-block;width:36px;height:2px;background:var(--red);vertical-align:middle;margin-right:6px}
.hero-dots{position:absolute;left:0;right:0;top:298px;display:flex;justify-content:center;gap:7px}
.hero-dots span{width:8px;height:8px;border-radius:50%;background:rgba(255,255,255,.5)}
.hero-dots span.on{background:var(--white)}

/* welcome */
.welcome{position:absolute;left:0;top:396px;width:736px;height:254px;background:var(--white)}
.welcome-title{position:absolute;left:100px;top:34px;display:flex;align-items:center;gap:10px}
.welcome-title .mark{width:34px;height:34px;background:var(--red)}
.welcome-title h1{font-family:"Marcellus",Georgia,serif;font-weight:400;color:var(--red);font-size:18px;line-height:21px}
.welcome-text{position:absolute;left:100px;top:84px;width:320px;font-size:8px;line-height:12px;color:var(--grey)}
.btn{position:absolute;left:100px;top:200px;background:var(--red);color:var(--white);font-size:8px;padding:4px 9px}
.photo-circle{position:absolute;border-radius:50%;border:5px solid var(--white);box-shadow:0 0 0 1px #ddd}

/* services band */
.services{position:absolute;left:0;top:650px;width:736px;height:245px;background:var(--red);display:flex;padding:0 60px}
.service{flex:1;text-align:center;color:var(--white);padding-top:26px}
.service .icon{width:60px;height:60px;margin:0 auto;display:block}
.service h2{font-family:"Marcellus",Georgia,serif;font-weight:400;font-size:15px;margin-top:14px}
.service p{font-size:8px;line-height:12px;margin:10px auto 0;width:170px;opacity:.9}
.service .dot{width:12px;height:12px;border-radius:50%;background:var(--white);margin:16px auto 0}

/* facilities + gallery */
.lower{position:absolute;left:0;top:895px;width:736px;height:160px;background:var(--white)}
.lower h3{font-family:"Marcellus",Georgia,serif;font-weight:400;font-size:18px;color:var(--ink)}
.facilities{position:absolute;left:100px;top:22px;width:200px}
.facilities ul{list-style:none;margin-top:12px}
.facilities li{font-size:8px;color:var(--grey);display:flex;align-items:center;gap:7px;height:16px}
.gallery{position:absolute;left:208px;top:22px}
.gallery-row{display:flex;gap:10px;margin-top:12px}
.gallery-item{width:136px;height:80px}
.gallery{left:280px}

/* footer */
.site-footer{position:absolute;left:0;top:1055px;width:736px;height:130px;background:var(--footer);display:flex;padding:14px 100px 0;gap:22px}
.footer-col{flex:1}
.footer-col h4{font-size:7px;font-weight:600;color:#ccc;text-transform:uppercase;letter-spacing:.5px;margin-bottom:9px;white-space:nowrap}
.footer-col ul{list-style:none}
.footer-col li{font-size:7px;color:#aaa;height:13px;display:flex;align-items:center;gap:6px;white-space:nowrap}
.map{width:100px;height:64px;background:linear-gradient(135deg,#d9d4c6,#c6cdb8 55%,#b9c4d0)}
.social-box{width:12px;height:12px;background:#555}
.footer-bottom{position:absolute;left:0;top:1185px;width:736px;height:15px;background:var(--footer-bottom);text-align:center;font-size:7px;line-height:15px;color:#888}
</style>
</head>
<body>

<header class="site-header">
  <div class="brand"><span class="brand-mark"></span><span class="brand-name">Corvane Architects</span></div>
  <div class="phone">
    <svg width="10" height="10" viewBox="0 0 24 24"><path fill="#c3202c" d="M6.6 10.8a15.1 15.1 0 0 0 6.6 6.6l2.2-2.2a1 1 0 0 1 1-.25 11.4 11.4 0 0 0 3.6.57 1 1 0 0 1 1 1V20a1 1 0 0 1-1 1A17 17 0 0 1 3 4a1 1 0 0 1 1-1h3.5a1 1 0 0 1 1 1c0 1.25.2 2.45.57 3.57a1 1 0 0 1-.25 1z"/></svg>
    020-7946-0318
  </div>
  <nav class="main-nav">
    <a class="active">Home</a><a>About</a><a>Services</a><a>Gallery</a><a>Contact</a>
  </nav>
</header>

<section class="hero" role="img" aria-label="Interior photograph of a warm timber and stone living room with a fireplace and wide windows">
  <p class="hero-caption serif"><span class="rule"></span>We Are An Architecture Practice That Specialises In One-off,<br>High End Homes And Commercial Properties</p>
  <div class="hero-dots"><span class="on"></span><span></span><span></span></div>
</section>

<section class="welcome">
  <div class="welcome-title"><span class="mark"></span><h1>Welcome to<br>Corvane Architects</h1></div>
  <p class="welcome-text">We design private residences and hospitality spaces shaped by landscape, craft and natural light. Each project begins with a careful study of the site, its views and the way our clients wish to live. Our studio works closely with builders and makers to deliver timber, stone and glass interiors of lasting quality, and every home is treated as a single, considered piece of architecture.</p>
  <span class="btn">Read More</span>
  <div class="photo-circle" role="img" aria-label="Photograph of a modern house with cantilevered terraces" style="left:420px;top:24px;width:140px;height:140px;background:radial-gradient(circle at 40% 40%,#c9d3dd,#8a9aa6 55%,#5e6b55)"></div>
  <div class="photo-circle" role="img" aria-label="Photograph of a house beside a pool under blue sky" style="left:520px;top:110px;width:112px;height:112px;background:linear-gradient(180deg,#7fb0d8,#c7d8e4 45%,#8b6a4a)"></div>
  <div class="photo-circle" role="img" aria-label="Photograph of a brick house among trees" style="left:440px;top:164px;width:76px;height:76px;background:linear-gradient(160deg,#7c8f5a,#8a5a3c)"></div>
</section>

<section class="services">
  <div class="service">
    <svg class="icon" viewBox="0 0 60 60"><circle cx="30" cy="30" r="28" fill="none" stroke="#fff" stroke-width="2"/><path d="M17 32 30 21l13 11M21 29v11h18V29" fill="none" stroke="#fff" stroke-width="2"/></svg>
    <h2>One Off</h2>
    <p>Unique homes drawn for a single site and family, with no repeated plans or stock details.</p>
    <div class="dot"></div>
  </div>
  <div class="service">
    <svg class="icon" viewBox="0 0 60 60"><circle cx="30" cy="30" r="28" fill="none" stroke="#fff" stroke-width="2"/><path d="M15 30 30 18l15 12M19 27v14h22V27M27 41v-7h6v7" fill="none" stroke="#fff" stroke-width="2"/></svg>
    <h2>High End Homes</h2>
    <p>Refined residences using fine timber, stone and glass for owners who value lasting quality.</p>
    <div class="dot"></div>
  </div>
  <div class="service">
    <svg class="icon" viewBox="0 0 60 60"><circle cx="30" cy="30" r="28" fill="none" stroke="#fff" stroke-width="2"/><path d="M20 42V20h20v22M24 25h4M32 25h4M24 31h4M32 31h4M27 42v-6h6v6" fill="none" stroke="#fff" stroke-width="2"/></svg>
    <h2>Commercial Properties</h2>
    <p>Restaurants and venues with warm interiors that welcome guests and serve busy teams.</p>
    <div class="dot"></div>
  </div>
</section>

<section class="lower">
  <div class="facilities">
    <h3>Our Facilities</h3>
    <ul>
      <li><svg width="9" height="9" viewBox="0 0 10 10"><path d="M1 5l3 3 5-6" fill="none" stroke="#c3202c" stroke-width="2"/></svg>Full site and feasibility studies</li>
      <li><svg width="9" height="9" viewBox="0 0 10 10"><path d="M1 5l3 3 5-6" fill="none" stroke="#c3202c" stroke-width="2"/></svg>Concept and detailed design</li>
      <li><svg width="9" height="9" viewBox="0 0 10 10"><path d="M1 5l3 3 5-6" fill="none" stroke="#c3202c" stroke-width="2"/></svg>Interior and furniture design</li>
      <li><svg width="9" height="9" viewBox="0 0 10 10"><path d="M1 5l3 3 5-6" fill="none" stroke="#c3202c" stroke-width="2"/></svg>Planning and council approvals</li>
      <li><svg width="9" height="9" viewBox="0 0 10 10"><path d="M1 5l3 3 5-6" fill="none" stroke="#c3202c" stroke-width="2"/></svg>Construction administration</li>
    </ul>
  </div>
  <div class="gallery">
    <h3>Our Gallery</h3>
    <div class="gallery-row">
      <div class="gallery-item" role="img" aria-label="Photograph of a low timber house in a green garden" style="background:linear-gradient(180deg,#b8c7c9,#7a6046 55%,#4f6a3a)"></div>
      <div class="gallery-item" role="img" aria-label="Photograph of a house set over a waterfall in autumn woods" style="background:linear-gradient(160deg,#c29a5c,#6f5a3a 50%,#3b3a30)"></div>
      <div class="gallery-item" role="img" aria-label="Photograph of a warm interior living space" style="background:linear-gradient(140deg,#4a2f22,#a06a3e 50%,#d6b183)"></div>
    </div>
  </div>
</section>

<footer class="site-footer">
  <div class="footer-col">
    <h4>Quick Links</h4>
    <ul><li>Home</li><li>About</li><li>Services</li><li>Gallery</li><li>Contact</li></ul>
  </div>
  <div class="footer-col">
    <h4>Contact Information</h4>
    <ul>
      <li><svg width="8" height="9" viewBox="0 0 10 12"><path d="M5 0a4 4 0 0 0-4 4c0 3 4 8 4 8s4-5 4-8a4 4 0 0 0-4-4z" fill="#c3202c"/></svg>48 Kestrel Lane, Marlow Bay</li>
      <li><svg width="8" height="8" viewBox="0 0 24 24"><path fill="#c3202c" d="M6.6 10.8a15.1 15.1 0 0 0 6.6 6.6l2.2-2.2a1 1 0 0 1 1-.25 11.4 11.4 0 0 0 3.6.57 1 1 0 0 1 1 1V20a1 1 0 0 1-1 1A17 17 0 0 1 3 4a1 1 0 0 1 1-1h3.5a1 1 0 0 1 1 1c0 1.25.2 2.45.57 3.57a1 1 0 0 1-.25 1z"/></svg>020-7946-0318</li>
      <li><svg width="9" height="7" viewBox="0 0 12 9"><rect x=".5" y=".5" width="11" height="8" fill="none" stroke="#c3202c"/><path d="M.5.5 6 5l5.5-4.5" fill="none" stroke="#c3202c"/></svg>studio@corvane.example</li>
    </ul>
  </div>
  <div class="footer-col">
    <h4>Contact Information</h4>
    <div class="map" role="img" aria-label="Street map showing the studio location"></div>
  </div>
  <div class="footer-col">
    <h4>Follow Us</h4>
    <ul>
      <li><span class="social-box"></span>Community</li>
      <li><span class="social-box"></span>Updates</li>
      <li><span class="social-box"></span>Network</li>
    </ul>
  </div>
</footer>
<div class="footer-bottom">Copyright 2013 Corvane Architects. All Rights Reserved.</div>

</body>
</html>
```